Need a stunning looking Business Card Design for my Telecom Business, Wow FACTOR!

I deal with high level IT Directors , and Contractors.
I need to impress them with a sleek , professional and unique business card.
Im thinking options as far as rounded edges, plastic , or even metal card or die cut on a corner.
Whatever looks better and leave an unforgettable first impression.
im looking for the wow factor.
Front should have the basics info (attached on the picture of current business card)
i would like to add picture of myself somewhere
Back side
should have logo and maybe some pictures or past projects, you can download from my website ( www.lumvexholdings.com)

```html
<!DOCTYPE html>
<html lang="en">
<head>
<meta charset="UTF-8">
<title>Lumvex Holdings – Business Card</title>
<link href="https://fonts.googleapis.com/css2?family=Open+Sans:wght@400;600;700&display=swap" rel="stylesheet">
<style>
  :root {
    --page-bg: #e6e1d9;
    --card-bg: #efe9df;
    --card-edge: #d8d0c2;
    --ink: #3a3a3c;
    --brand-navy: #1f3f6e;
    --accent-teal: #2a93b0;
    --band-start: #2689a8;
    --band-end: #2f9cb8;
    --band-text: #e4ddd0;
    --photo-ring: #dcd3c4;
    --photo-fill: #8b8983;
  }
  * { margin: 0; padding: 0; box-sizing: border-box; }
  html, body {
    width: 1200px;
    height: 1000px;
    overflow: hidden;
    background: var(--page-bg);
    font-family: "Open Sans", Arial, sans-serif;
  }
  .business-card {
    position: absolute;
    left: 146px;
    top: 265px;
    width: 956px;
    height: 520px;
    background: var(--card-bg);
    border: 1px solid var(--card-edge);
    border-radius: 6px;
    overflow: hidden;
  }
  .brand {
    position: absolute;
    left: 78px;
    top: 200px;
    display: flex;
    align-items: center;
    gap: 14px;
  }
  .brand-dot {
    width: 22px;
    height: 22px;
    border-radius: 50%;
    background: var(--brand-navy);
  }
  .brand-name {
    font-weight: 600;
    font-size: 34px;
    letter-spacing: 3px;
    color: var(--brand-navy);
    text-transform: uppercase;
  }
  .contact-list {
    position: absolute;
    left: 558px;
    top: 126px;
    list-style: none;
  }
  .contact-item {
    display: flex;
    align-items: center;
    height: 38px;
    font-size: 22px;
    color: var(--ink);
  }
  .contact-icon {
    width: 24px;
    height: 24px;
    margin-right: 19px;
    flex: none;
  }
  .identity-band {
    position: absolute;
    left: 0;
    top: 320px;
    width: 100%;
    height: 147px;
    background: linear-gradient(90deg, var(--band-start), var(--band-end));
  }
  .person-name {
    position: absolute;
    left: 72px;
    top: 37px;
    font-weight: 700;
    font-size: 35px;
    color: var(--band-text);
    letter-spacing: 0.5px;
  }
  .person-role {
    position: absolute;
    left: 72px;
    top: 88px;
    font-size: 20px;
    color: var(--band-text);
    text-transform: uppercase;
  }
  .portrait {
    position: absolute;
    left: 618px;
    top: 298px;
    width: 212px;
    height: 212px;
    border-radius: 50%;
    border: 5px solid var(--photo-ring);
    background: radial-gradient(circle at 50% 40%, #a29e96, var(--photo-fill));
  }
</style>
</head>
<body>
  <div class="business-card">
    <div class="brand">
      <span class="brand-dot"></span>
      <span class="brand-name">Lumvex Holdings</span>
    </div>

    <ul class="contact-list">
      <li class="contact-item">
        <svg class="contact-icon" viewBox="0 0 24 24" fill="none" stroke="var(--accent-teal)" stroke-width="1.6" stroke-linejoin="round">
          <path d="M6 3l3 4-2 2c1 3 4 6 7 7l2-2 4 3-2 3C10 20 4 14 3 6z"/>
        </svg>
        (555) 318-4702
      </li>
      <li class="contact-item">
        <svg class="contact-icon" viewBox="0 0 24 24" fill="none" stroke="var(--accent-teal)" stroke-width="1.6">
          <rect x="2" y="5" width="20" height="14"/>
          <path d="M2 5l10 8 10-8"/>
        </svg>
        info@lumvexholdings.com
      </li>
      <li class="contact-item">
        <svg class="contact-icon" viewBox="0 0 24 24" fill="none" stroke="var(--accent-teal)" stroke-width="1.6">
          <circle cx="12" cy="12" r="10"/>
          <ellipse cx="12" cy="12" rx="4.5" ry="10"/>
          <path d="M2 12h20M4 7h16M4 17h16"/>
        </svg>
        lumvexholdings.com
      </li>
    </ul>

    <div class="identity-band">
      <div class="person-name">REN TAKEDA</div>
      <div class="person-role">Operations Manager</div>
    </div>

    <div class="portrait" role="img" aria-label="Portrait photo of the card holder"></div>
  </div>
</body>
</html>
```